Brookhaven Kitchens Stationary
Stationary Set with Business Card
Project: Brookhaven Kitchens Stationary
Brookhaven Kitchens Stationary - Chef / Catering
Creative Brief
Professional
Daniel Hensley
Chef/Owner
4738 W. Marlow Ave Orlando, FL 32899
dan@brookhavenkitchens.example
www.brookhavenkitchens.example
Simple with the BK (circle) part of the logo on the back, like a branding iron

```html
<!DOCTYPE html>
<html lang="en">
<head>
<meta charset="utf-8">
<title>Brookhaven Kitchens – Business Card Options</title>
<link rel="stylesheet" href="https://fonts.googleapis.com/css2?family=Open+Sans:ital,wght@0,400;0,600;1,400&family=Michroma&display=swap">
<style>
  :root{
    --backdrop:#2f2f2f;
    --card-light:#ffffff;
    --card-dark:#3a3939;
    --rust:#a8482a;
    --rust-light:#c8683d;
    --tan:#b8a68f;
    --ink:#6a6a6a;
    --ink-light:#cfcfcf;
    --label:#e6e6e6;
  }
  *{margin:0;padding:0;box-sizing:border-box}
  html,body{width:1200px;height:809px;overflow:hidden;background:var(--backdrop)}
  .sheet{position:relative;width:1200px;height:809px;background:radial-gradient(circle at 50% 40%,#3a3a3a,#262626)}
  .card{position:absolute;width:498px;height:288px;border-radius:14px;overflow:hidden}
  .card--light{background:var(--card-light)}
  .card--dark{background:var(--card-dark)}
  .front-a{left:72px;top:43px}
  .front-b{left:636px;top:43px}
  .back-a{left:72px;top:424px}
  .back-b{left:636px;top:424px}

  .brand{position:absolute;left:40px;top:70px;width:190px;text-align:center}
  .brand-ring{display:block;margin:0 auto 10px;width:72px;height:72px;border-radius:50%;border:3px solid var(--tan)}
  .brand-name{font-family:"Open Sans",sans-serif;font-weight:600;font-size:19px;color:var(--rust);line-height:1.15}

  .divider{position:absolute;left:262px;top:22px;width:1px;height:205px;background:#d9d2c8}
  .card--dark .divider{background:#5a5656}

  .contact{position:absolute;left:280px;top:20px;font-family:"Open Sans",sans-serif}
  .contact-name{font-style:italic;font-size:15px;color:var(--rust)}
  .card--dark .contact-name{color:var(--ink-light)}
  .contact-role{font-size:10px;color:var(--ink);margin-bottom:18px}
  .card--dark .contact-role{color:#aaa}
  .contact-row{display:flex;align-items:center;gap:7px;font-size:10px;color:var(--ink);height:27px}
  .card--dark .contact-row{color:var(--ink-light)}
  .contact-row svg{width:11px;height:11px;flex:none}
  .icon{fill:var(--rust)}

  .band{position:absolute;left:0;bottom:0;width:100%;height:36px;background:linear-gradient(90deg,var(--rust),var(--rust-light));
        font-family:"Open Sans",sans-serif;font-size:11px;letter-spacing:2px;color:#fff;text-align:center;line-height:36px}
  .card--light .band{border-top:3px solid #e4d8cc}

  .emblem{position:absolute;left:50%;top:50%;transform:translate(-50%,-50%);text-align:center}
  .emblem-ring{display:block;margin:0 auto 12px;width:150px;height:150px;border-radius:50%;border:6px solid var(--tan)}
  .emblem-name{font-family:"Open Sans",sans-serif;font-weight:600;font-size:20px;color:var(--tan)}

  .label{position:absolute;width:498px;text-align:center;font-family:"Michroma",sans-serif;font-size:15px;letter-spacing:3px;color:var(--label)}
  .label-fa{left:72px;top:360px}
  .label-fb{left:636px;top:360px}
  .label-ba{left:72px;top:724px}
  .label-bb{left:636px;top:724px}
</style>
</head>
<body>
<div class="sheet">

  <section class="card card--light front-a">
    <div class="brand"><span class="brand-ring"></span><div class="brand-name">Brookhaven Kitchens</div></div>
    <div class="divider"></div>
    <div class="contact">
      <div class="contact-name">Daniel Hensley</div>
      <div class="contact-role">Chef/Owner</div>
      <div class="contact-row"><svg viewBox="0 0 12 12"><circle class="icon" cx="6" cy="6" r="5.5"/></svg>www.brookhavenkitchens.example</div>
      <div class="contact-row"><svg viewBox="0 0 12 12"><path class="icon" d="M2 1h3l1 3-2 1a6 6 0 0 0 3 3l1-2 3 1v3c-6 0-9-3-9-9z"/></svg>407-555-0148</div>
      <div class="contact-row"><svg viewBox="0 0 12 12"><path class="icon" d="M1 3h10v7H1z"/></svg>dan@brookhavenkitchens.example</div>
      <div class="contact-row"><svg viewBox="0 0 12 12"><path class="icon" d="M6 0a4 4 0 0 1 4 4c0 3-4 8-4 8S2 7 2 4a4 4 0 0 1 4-4z"/></svg>4738 W. Marlow Ave Orlando, FL 32899</div>
    </div>
    <div class="band">www.brookhavenkitchens.example</div>
  </section>

  <section class="card card--dark front-b">
    <div class="brand"><span class="brand-ring"></span><div class="brand-name">Brookhaven Kitchens</div></div>
    <div class="divider"></div>
    <div class="contact">
      <div class="contact-name">Daniel Hensley</div>
      <div class="contact-role">Chef/Owner</div>
      <div class="contact-row"><svg viewBox="0 0 12 12"><circle class="icon" cx="6" cy="6" r="5.5"/></svg>www.brookhavenkitchens.example</div>
      <div class="contact-row"><svg viewBox="0 0 12 12"><path class="icon" d="M2 1h3l1 3-2 1a6 6 0 0 0 3 3l1-2 3 1v3c-6 0-9-3-9-9z"/></svg>407-555-0148</div>
      <div class="contact-row"><svg viewBox="0 0 12 12"><path class="icon" d="M1 3h10v7H1z"/></svg>dan@brookhavenkitchens.example</div>
      <div class="contact-row"><svg viewBox="0 0 12 12"><path class="icon" d="M6 0a4 4 0 0 1 4 4c0 3-4 8-4 8S2 7 2 4a4 4 0 0 1 4-4z"/></svg>4738 W. Marlow Ave Orlando, FL 32899</div>
    </div>
    <div class="band">www.brookhavenkitchens.example</div>
  </section>

  <div class="label label-fa">Business Card Front Option A</div>
  <div class="label label-fb">Business Card Front Option B</div>

  <section class="card card--light back-a">
    <div class="emblem"><span class="emblem-ring"></span><div class="emblem-name">Brookhaven</div></div>
  </section>

  <section class="card card--dark back-b">
    <div class="emblem"><span class="emblem-ring"></span><div class="emblem-name">Brookhaven</div></div>
  </section>

  <div class="label label-ba">Business Card Back Option A</div>
  <div class="label label-bb">Business Card Back Option B</div>

</div>
</body>
</html>
```